Hexagon Honey Bottle Design, simple and elegant.

Bottle description:
BODY HEIGHT With cap 8.75cm
Without cap 8.6cm
DIAMETER Inner 4.4cm
Outer 5.2cm
Label height only has to be = 6cm height x (3.4X6) length of one hexagonal box is 3.4cm
See through bottle with black cap.
Concept of design:
Elegant, Simple, no pictures of bees, pictures of honeycomb, wooden honey stick, or drooling honey from either is ok. Simple colors. (Designer's discretion)
Wordings:
Hex1
Product of Yemen
Header:
KORVAL /MELO/ (Brand name)
Explanatory below header
Yemen Sidr Honey from The Valley Ra'ufil (100% Pure)
(name of honey)
250g
Optional
Hex2
Pure
=
No Additives (not even natural additives)
Hex3
Raw
=
Unheated, Unpasteurized, Unprocessed honey
Hex4
Natural
=
No added color, artificial flavor, or synthetic substance
Hex5
RENOWNED
=
Very well known by honey lovers
(Natural Pure Raw and Renowned) wordings to be on a suitable place on the bottle (maybe on the cap) -
Hex6
Imported By
The Lantern Bazaar Pte Ltd
No. 317, Cobalt Ferry Road, #09-12
Cobalt Ferry Plaza
Singapore 195340
Wordings can be rearranged - its up to the designer's discretion where and how to place them and in which order.-
Designer must be willing to do numerous changes as the design develops

```html
<!DOCTYPE html>
<html lang="en">
<head>
<meta charset="utf-8">
<title>KORVAL Yemen Sidr Honey – Hexagon Jar Label</title>
<link rel="stylesheet" href="https://fonts.googleapis.com/css2?family=Oswald:wght@300;400;500;600&family=Josefin+Sans:wght@300;400&family=Dancing+Script:wght@400&display=swap">
<style>
  :root {
    --honey-yellow: #e9c41f;
    --label-charcoal: #393939;
    --cap-black: #1d1a19;
    --cap-gold: #a88c3c;
    --paper-white: #ffffff;
    --stage-bg: #ecebe7;
  }
  * { box-sizing: border-box; margin: 0; padding: 0; }
  html, body { width: 1200px; height: 894px; overflow: hidden; }
  body {
    background: var(--stage-bg);
    font-family: "Oswald", sans-serif;
    position: relative;
  }

  /* Cap lid band */
  .cap-band {
    position: absolute;
    left: 300px; top: 200px;
    width: 600px; height: 64px;
    background: var(--cap-black);
    border-radius: 14px;
    display: flex; align-items: center; justify-content: center;
  }
  .cap-band__motto {
    font-family: "Josefin Sans", sans-serif;
    font-weight: 400;
    font-size: 24px;
    color: var(--cap-gold);
    letter-spacing: 0.5px;
  }

  /* Unrolled hexagonal label: six faces */
  .label-wrap {
    position: absolute;
    left: 30px; top: 330px;
    width: 1140px; height: 335px;
    display: flex;
  }
  .face {
    position: relative;
    width: 190px; height: 335px;
    text-align: center;
  }
  .face--dark { background: var(--label-charcoal); color: var(--paper-white); }
  .face--yellow { background: var(--honey-yellow); color: var(--label-charcoal); }

  /* Attribute word headings */
  .attribute {
    position: absolute; left: 0; right: 0; top: 112px;
    font-family: "Oswald", sans-serif;
    font-weight: 500;
    font-size: 20px;
    letter-spacing: 3px;
    line-height: 28px;
  }
  .face--dark .attribute { color: var(--honey-yellow); }
  .face--yellow .attribute { color: var(--label-charcoal); }

  .equals-mark {
    position: absolute; left: 0; right: 0; top: 158px;
    font-size: 16px; font-weight: 600;
  }
  .meaning {
    position: absolute; left: 10px; right: 10px; top: 192px;
    font-family: "Dancing Script", cursive;
    font-size: 13px; line-height: 1.45;
  }

  /* Front face */
  .front__origin {
    position: absolute; left: 0; right: 0; top: 11px;
    font-family: "Josefin Sans", sans-serif; font-size: 9px; color: var(--paper-white);
  }
  .front__rule {
    position: absolute; left: 50px; right: 50px; top: 24px;
    height: 1px; background: var(--paper-white);
  }
  .front__brand {
    position: absolute; left: 0; right: 0; top: 28px;
    font-family: "Josefin Sans", sans-serif; font-weight: 300;
    font-size: 24px; letter-spacing: 4px; color: var(--paper-white);
  }
  .front__dipper {
    position: absolute; left: 10px; top: 92px; width: 48px; height: 150px;
  }
  .front__purity {
    position: absolute; left: 74px; top: 92px;
    font-weight: 300; font-size: 15px;
  }
  .front__stick {
    position: absolute; left: 52px; right: 0; top: 114px;
    height: 3px; background: var(--label-charcoal);
  }
  .front__name {
    position: absolute; right: 16px; top: 122px;
    text-align: right; font-weight: 600; font-size: 37px; line-height: 1.02;
    transform: scaleX(0.85); transform-origin: right top;
  }
  .front__weight {
    position: absolute; left: 120px; top: 207px;
    width: 50px; height: 20px; border-radius: 10px;
    background: var(--label-charcoal); color: var(--honey-yellow);
    font-style: italic; font-weight: 300; font-size: 15px; line-height: 20px;
  }
  .front__variety {
    position: absolute; left: 0; right: 0; top: 278px;
    font-weight: 300; font-size: 17px; line-height: 1.1;
  }
  .front__valley { display: block; font-size: 12px; }

  /* Importer face */
  .importer {
    position: absolute; left: 4px; right: 4px; top: 120px;
    color: var(--honey-yellow);
    font-weight: 300; font-size: 11.5px; line-height: 24px;
  }
  .importer__title { font-weight: 500; font-size: 12px; }
</style>
</head>
<body>

  <div class="cap-band">
    <p class="cap-band__motto">Natural Pure Raw and Renowned</p>
  </div>

  <div class="label-wrap">

    <section class="face face--dark">
      <h2 class="attribute">NATURAL</h2>
      <p class="equals-mark">=</p>
      <p class="meaning">No added color,<br>artificial flavor,<br>or synthetic substance</p>
    </section>

    <section class="face face--yellow">
      <p class="front__origin">Product of Yemen</p>
      <div class="front__rule"></div>
      <p class="front__brand">KORVAL</p>
      <svg class="front__dipper" viewBox="0 0 48 150" role="img" aria-label="White honey dipper with dripping honey">
        <rect x="0" y="0" width="48" height="150" fill="#f3dc72"/>
      </svg>
      <p class="front__purity">100% PURE</p>
      <div class="front__stick"></div>
      <h1 class="front__name">NATURAL<br>HONEY</h1>
      <p class="front__weight">250g</p>
      <p class="front__variety">Yemen Sidr Honey<span class="front__valley">from The Valley Ra'ufil</span></p>
    </section>

    <section class="face face--dark">
      <h2 class="attribute">PURE</h2>
      <p class="equals-mark">=</p>
      <p class="meaning">No Additives<br>(not even natural additives)</p>
    </section>

    <section class="face face--yellow">
      <h2 class="attribute">RENOWNED</h2>
      <p class="equals-mark">=</p>
      <p class="meaning">Very well known<br>by<br>honey lovers</p>
    </section>

    <section class="face face--dark">
      <div class="importer">
        <p class="importer__title">IMPORTED BY</p>
        <p>The Lantern Bazaar Pte Ltd</p>
        <p>No. 317, Cobalt Ferry Road, #09-12</p>
        <p>Cobalt Ferry Plaza</p>
        <p>Singapore 195340</p>
      </div>
    </section>

    <section class="face face--yellow">
      <h2 class="attribute">RAW</h2>
      <p class="equals-mark">=</p>
      <p class="meaning">Unheated,<br>Unpasteurized,<br>Unprocessed honey</p>
    </section>

  </div>

</body>
</html>
```